refurbishment of diamond cut alloy wheels

we need to design a flyer that will catch the eye of the customer to refurbish diamond cut alloy wheels. we refurbish the wheels by using the latest CNC machine to precision cut and resurface the wheel. we would like before and after pictures of maybe Kelvaron, DXT, Orsa wheels to give it a prestige look. The final design should communicate an expensive look and providing a good image for the business. The colours that I would like to use is black and red which should make the flyer stand out. The logo must sit on a black background without the wordings of specialists in HJ, Orsa etc and also without servicing, diagnostics etc as well. This flyer is just to communicate refurbishment of alloy wheels to high standard.

Target Market(s)

any members of the public and car dealerships

Industry/Entity Type

Automotive

Colors

Designer to choose colors to be used in the design.

Requirements
Must have
• Wow factor with great images of wheels
Nice to have
• Maybe on the front of the flyer it has a picture of a wheel and then on the back of the flyer it has before and after pictures to show how just how incredible it is to refurbish wheels
Should not have
• other makes of wheels apart from DXT, Orsa, and any other high end makes of vehicles wheels

```html
<!DOCTYPE html>
<html lang="en">
<head>
<meta charset="utf-8">
<title>Crestline Motors – Diamond Cut Alloy Refurbishment Flyer</title>
<link rel="stylesheet" href="https://fonts.googleapis.com/css2?family=Russo+One&family=Questrial&display=swap">
<style>
  :root {
    --stage: #d4d4d4;
    --red-deep: #5a0207;
    --red-mid: #9a0a12;
    --red-bright: #d8141d;
    --black: #0b0b0d;
    --white: #ffffff;
    --label-yellow: #f2e33a;
    --frame: #f4d6d6;
  }
  * { box-sizing: border-box; margin: 0; padding: 0; }
  html, body { width: 926px; height: 1200px; overflow: hidden; }
  body {
    background: var(--stage);
    font-family: "Questrial", sans-serif;
    color: var(--white);
    position: relative;
  }
  .spread {
    position: absolute;
    top: 303px;
    left: 30px;
    display: flex;
    gap: 26px;
  }
  .page {
    width: 420px;
    height: 594px;
    position: relative;
    overflow: hidden;
    box-shadow: 0 4px 12px rgba(0,0,0,.35);
    background:
      linear-gradient(115deg, transparent 0 30%, rgba(255,60,60,.18) 30% 38%, transparent 38% 55%, rgba(255,40,40,.14) 55% 60%, transparent 60%),
      linear-gradient(160deg, var(--red-mid) 0%, var(--red-deep) 45%, var(--red-bright) 100%);
  }
  .page--back {
    background:
      linear-gradient(120deg, transparent 0 45%, rgba(255,70,70,.16) 45% 52%, transparent 52% 68%, rgba(255,60,60,.2) 68% 76%, transparent 76%),
      linear-gradient(150deg, var(--red-deep) 0%, var(--red-mid) 50%, var(--red-bright) 100%);
  }
  .brand {
    display: flex;
    align-items: center;
    gap: 7px;
    font-family: "Questrial", sans-serif;
    font-size: 17px;
    letter-spacing: .5px;
    color: var(--white);
  }
  .brand__mark {
    width: 14px; height: 14px;
    background: var(--white);
  }
  .page--front .brand {
    position: absolute; top: 44px; left: 0; right: 0;
    justify-content: center;
  }
  .headline {
    position: absolute; top: 102px; left: 0; right: 0;
    text-align: center;
    font-family: "Russo One", sans-serif;
    font-size: 31px;
    line-height: 36px;
    text-transform: uppercase;
    transform: skewX(-12deg);
    text-shadow: 0 2px 3px rgba(0,0,0,.6);
  }
  .hero-photo {
    position: absolute; left: 0; right: 0; top: 215px; bottom: 0;
    background: radial-gradient(circle at 42% 40%, #5b5d63 0%, #2b2c31 30%, #121215 60%, #050506 100%);
  }
  .hero-photo::before {
    content: ""; position: absolute; inset: 0;
    background: linear-gradient(180deg, rgba(130,8,14,.85) 0%, rgba(90,2,7,.3) 30%, transparent 55%);
  }
  .back-title {
    padding-top: 20px;
    text-align: center;
    font-family: "Russo One", sans-serif;
    font-size: 13px;
    line-height: 22px;
    text-transform: uppercase;
    letter-spacing: .5px;
    transform: skewX(-12deg);
  }
  .copy {
    margin: 22px 38px 0 50px;
    font-size: 8.4px;
    line-height: 13.8px;
    text-align: justify;
  }
  .copy p + p { margin-top: 13px; }
  .compare {
    position: absolute; top: 248px; left: 51px;
    width: 312px; height: 216px;
    border: 1px solid var(--frame);
    padding: 5px;
    display: flex;
    gap: 2px;
  }
  .compare__shot {
    flex: 1; position: relative;
  }
  .compare__shot--before { background: radial-gradient(circle at 55% 55%, #b9b6b0 0%, #6d6b68 45%, #1c1b1a 80%); }
  .compare__shot--after { background: radial-gradient(circle at 45% 55%, #dcdcdc 0%, #9a9a9c 45%, #1a1a1b 80%); }
  .compare__label {
    position: absolute; top: 2px;
    font-family: "Times New Roman", serif;
    font-size: 9.5px;
    color: var(--label-yellow);
    text-transform: uppercase;
  }
  .compare__shot--before .compare__label { left: 6px; }
  .compare__shot--after .compare__label { left: 6px; }
  .contact {
    position: absolute; top: 488px; left: 228px;
    font-size: 8.6px;
    line-height: 13px;
  }
  .contact__lines { margin-top: 14px; }
  .contact__row { display: flex; align-items: center; gap: 4px; }
  .contact__row svg { width: 8px; height: 8px; fill: var(--white); }
  .page--back .brand {
    position: absolute; top: 530px; left: 40px;
  }
</style>
</head>
<body>
  <main class="spread">
    <section class="page page--front">
      <div class="hero-photo" role="img" aria-label="Close-up photograph of a dark graphite diamond cut alloy wheel with fine spokes"></div>
      <div class="brand"><span class="brand__mark"></span>Crestline Motors</div>
      <h1 class="headline">Refurbish<br>Diamond Cut<br>Alloy Wheels</h1>
    </section>

    <section class="page page--back">
      <h2 class="back-title">Alloy Refurbishment Specialists<br>in and around Ashmere</h2>
      <div class="copy">
        <p>If you are looking to refresh the look of your car but don't want the expense of new alloys, with a wide range of limited edition colours to choose from why not consider customising and refurbishing your existing alloys?</p>
        <p>If you've had your alloy wheels long enough for them to require alloy refurbishment you can choose from a wide range of colours for refurbishment or choose a brand new set from our comprehensive range. At Northgate Wheels &amp; Tyres, we stock an extensive range of the latest designs from all the leading suppliers and manufacturers so you are sure to find a stylish new design.</p>
      </div>
      <div class="compare">
        <div class="compare__shot compare__shot--before" role="img" aria-label="DXT alloy wheel with scuffed, corroded rim before refurbishment"><span class="compare__label">Before</span></div>
        <div class="compare__shot compare__shot--after" role="img" aria-label="The same DXT alloy wheel gleaming silver after refurbishment"><span class="compare__label">After</span></div>
      </div>
      <div class="brand"><span class="brand__mark"></span>Crestline Motors</div>
      <address class="contact" style="font-style:normal">
        <div>14B Hawthorn Lane,<br>Ashmere,<br>Berkshire, AS9 2QT</div>
        <div class="contact__lines">
          <div class="contact__row"><svg viewBox="0 0 10 10"><path d="M2 0h2l1 3-1.5 1a6 6 0 0 0 2.5 2.5L7 5l3 1v2a2 2 0 0 1-2 2A8 8 0 0 1 0 2a2 2 0 0 1 2-2z"/></svg>01632 960418</div>
          <div class="contact__row"><svg viewBox="0 0 10 10"><rect x="2" y="0" width="6" height="3"/><rect x="0" y="3.5" width="10" height="4"/><rect x="2" y="7" width="6" height="3"/></svg>01632 960419</div>
          <div class="contact__row"><svg viewBox="0 0 10 10"><path d="M0 2h10v6H0z M0 2l5 3.5L10 2" fill="none" stroke="#fff" stroke-width="1.2"/></svg>hello@crestlinemotors.example</div>
        </div>
      </address>
    </section>
  </main>
</body>
</html>
```